Corporate Design für Frauenärztinnen am Talbrunnen gesucht
Ansprechendes,erfrischendes Design, dass sich angenehm von den anderen Entwürfen abgesetzt hat. Kleine Korrekturen wurden prompt und gut umgesetzt. Hat Spass gebracht.
Zielgruppe
Wir sind eine reguläre Frauenarztpraxis. Unsere Zielgruppe sind junge Frauen, Schwangere, junge Mädchen, mittelalte bis alte Patientinnen.
Aufgabenstellung
Ich wünsche mir für meine Praxis ein modernes und schlichtes Design, das anspricht. Es sollte nicht 'zu viel los sein' und einge gewisse Ruhe und Gelassenheit ausstrahlen.

```html
<!DOCTYPE html>
<html lang="de">
<head>
<meta charset="utf-8">
<title>Frauenärztinnen am Talbrunnen – Visitenkarte</title>
<link rel="stylesheet" href="https://fonts.googleapis.com/css2?family=Encode+Sans+Condensed:wght@300;400&family=Jost:wght@300;400&display=swap">
<style>
  :root {
    --bg: #ececec;
    --paper: #ffffff;
    --blue-deep: #1f6a8f;
    --blue-mid: #4e93b6;
    --blue-light: #a7cfe0;
    --band: #79adc4;
    --ink: #5c8ea8;
    --icon: #6f9cb3;
    --ring: #2f6e8e;
  }
  * { box-sizing: border-box; margin: 0; padding: 0; }
  html, body { width: 1200px; height: 800px; overflow: hidden; background: var(--bg); }
  .canvas {
    width: 1200px; height: 800px;
    display: flex; align-items: center; justify-content: center; gap: 60px;
  }
  .card {
    width: 510px; height: 330px; position: relative; overflow: hidden;
    border-radius: 3px;
    box-shadow: 0 2px 3px rgba(0,0,0,.08), 0 12px 30px rgba(0,0,0,.10);
  }

  /* Front */
  .card--front {
    background: linear-gradient(170deg, var(--blue-mid) 0%, var(--blue-light) 40%, var(--blue-mid) 65%, var(--blue-deep) 100%);
    display: flex; flex-direction: column; align-items: center; justify-content: center;
    color: #eef5f8; font-family: "Jost", sans-serif; text-align: center;
  }
  .wordmark__dot {
    width: 62px; height: 62px; border-radius: 50%;
    border: 2px solid #eef5f8; margin-bottom: 26px;
  }
  .wordmark__name { font-size: 30px; font-weight: 400; letter-spacing: .16em; text-transform: uppercase; }
  .wordmark__place { font-size: 30px; font-weight: 400; letter-spacing: .16em; text-transform: uppercase; margin-top: 6px; }

  /* Back */
  .card--back { background: var(--paper); font-family: "Encode Sans Condensed", sans-serif; }
  .name-band {
    height: 52px; background: var(--band); color: #fff;
    display: flex; align-items: center; padding-left: 34px;
    font-size: 24px; font-weight: 300; letter-spacing: .04em; text-transform: uppercase;
  }
  .contact-list { list-style: none; padding: 28px 0 0 34px; }
  .contact-list li {
    display: flex; align-items: center; gap: 14px;
    color: var(--ink); font-size: 20px; font-weight: 300; line-height: 1; margin-bottom: 18px;
  }
  .contact-list svg { width: 20px; height: 20px; flex: none; fill: var(--icon); }
  .deco-ring {
    position: absolute; right: 40px; bottom: -70px;
    width: 190px; height: 190px; border-radius: 50%;
    border: 4px solid var(--ring);
  }
</style>
</head>
<body>
<main class="canvas">
  <section class="card card--front" aria-label="Vorderseite">
    <div class="wordmark__dot"></div>
    <p class="wordmark__name">Frauenärztinnen</p>
    <p class="wordmark__place">am Talbrunnen</p>
  </section>

  <section class="card card--back" aria-label="Rückseite">
    <header class="name-band">Dr. Lena Albrecht</header>
    <ul class="contact-list">
      <li>
        <svg viewBox="0 0 20 20" aria-hidden="true"><circle cx="10" cy="10" r="10"/><path d="M5 7h10v6H5z" fill="#fff"/><path d="M5 7l5 4 5-4" stroke="#6f9cb3" stroke-width="1.2" fill="none"/></svg>
        info@fa-am-talbrunnen.de
      </li>
      <li>
        <svg viewBox="0 0 20 20" aria-hidden="true"><path d="M5 2c1 0 2 3 2 4s-1.5 1.2-1 2.5c1 2 2.5 3.5 4.5 4.5 1.3.5 1.5-1 2.5-1s4 1 4 2-1 3-3 3C8 17 3 12 3 5c0-2 1-3 2-3z"/></svg>
        +49 0421 5550198
      </li>
      <li>
        <svg viewBox="0 0 20 20" aria-hidden="true"><path d="M10 2l8 7h-2.5v8h-4v-5h-3v5h-4V9H2z"/></svg>
        Brunnenweg 4, 28195 Talstadt
      </li>
      <li>
        <svg viewBox="0 0 20 20" aria-hidden="true"><circle cx="10" cy="10" r="10"/><path d="M10 1v18M1 10h18M10 1c-4 4-4 14 0 18M10 1c4 4 4 14 0 18" stroke="#fff" stroke-width="1.1" fill="none"/></svg>
        www.fa-am-talbrunnen.de
      </li>
    </ul>
    <div class="deco-ring" aria-hidden="true"></div>
  </section>
</main>
</body>
</html>
```